The Quiet Ascent Book Cover

Book Title:
The Quiet Ascent: Lessons of Insight From A Circle of Mentors to Guide You Toward a Fuller Journey

This book will offer the wisdom and philosophies of a variety of different coaches to allow future clients to get a taste of you and your style and prepare them to work with you!

A coach does not fix you. Or heal you. They coach you - offer thoughts to ponder, guidance, techniques to try. All to help you plays and succeed at the game of life.

Each coach has their own personality, training, experience, method and philosophy they bring to the table. The underlying purpose is to guide you through The Quiet Ascent, to become the person you desire and aspire to be. Different coaches for different folks, yet they all have their own unique wisdom and special sauce to share.

This book is a collection of just that. A tasting of the wisdom and philosophies of a variety of different coaches for you to experience.

Types of Coaches: Clarity, Dreams, Goals, Motivation, Mindset,  Subconscious, Beliefs, Behavior, Accountability, Life, Wellness, Love & Dating, Relationships, Sex, Business, Career,  Executive,  Personal Development,  Writing, Wellness, Fitness, Parenting,  Style, Spirituality, Public Speaking, Financial,  Time management, Weight Loss, Running, Self esteem,  Tarot, Astrology, Enneagram, Soul path/ Dharma, Skills, Performance,  Speaking / Communication, Leadership, Shadow Work, Acting, Sports, ANY & ALL

Target Market(s)

Males or females looking for guidance and words of wisdom from an expert coach - maybe to find one that resonates with them to work with further. Ages 16 and up. Any Gender. International. Looking to improve their life!

Industry/Entity Type

Self Development, Wellness, Coaching, Personal Growth, Fitness, Spirituality, Business, Relationships

Font styles to use
Serif
Script

Colors
0054AA
0677BA
7BADD7
CADEEF
E8F1F8
FFF300
FFF600
FEFA6F
FFFEC7
FFFEE8

Requirements
Must have
• I am looking for a visually appealing, unique cover that encompasses the breadth and depth of the transformation that people can go through and inspires them to want to grow and change even more. I love when elegant and classic simplicity is combined with some kind of twist that catches the eye and provokes thought. I love complimentary fonts, colors, design elements. You can visit my Veltrano Author Page - Dr. Marisol Penbury Aldane to see my titles to see what I have liked! But I am also excited to see where you can make my vision even better!!
Nice to have
• Front Cover - Image, Title and Subtitle, The Lark Publishing House, Spine - Title and Publishing House Logo, Back - Book Blurb, Authors Names, Info about Publishing House, ISBN Barcode
Should not have
• Anything too feminine or too masculine as I want to encourage coaches of all genders to participate.

```html
<!DOCTYPE html>
<html lang="en">
<head>
<meta charset="utf-8">
<title>The Quiet Ascent — Book Cover</title>
<link href="https://fonts.googleapis.com/css2?family=Bodoni+Moda:wght@400;600&family=Playfair+Display:wght@700&family=Great+Vibes&family=Outfit:wght@400&display=swap" rel="stylesheet">
<style>
  :root{
    --paper:#c3c3c1;
    --ink:#0a0a0a;
    --white:#ffffff;
    --navy:#2a3560;
    --wing-deep:#0b1a3c;
    --wing-bright:#1f8fc8;
  }
  *{margin:0;padding:0;box-sizing:border-box}
  html,body{width:1200px;height:831px;overflow:hidden;background:var(--paper)}
  .cover{position:relative;width:1200px;height:831px;background:var(--paper);overflow:hidden}

  /* back cover */
  .back-title{position:absolute;left:0;width:556px;top:84px;text-align:center;
    font-family:"Bodoni Moda",serif;font-weight:600;font-size:27px;line-height:24px;letter-spacing:1.5px;color:var(--ink);
    transform:scaleX(.86);transform-origin:278px 0}
  .back-subtitle{position:absolute;left:0;width:556px;top:111px;text-align:center;
    font-family:"Bodoni Moda",serif;font-size:9.5px;line-height:10px;letter-spacing:.6px;text-transform:uppercase;color:var(--ink)}
  .blurb{position:absolute;left:97px;width:359px;top:158px;font-family:"Outfit",sans-serif;font-size:11.4px;line-height:14.75px;color:var(--white);text-align:justify}
  .blurb p{margin-bottom:14.6px}
  .authors-heading{position:absolute;left:0;width:556px;top:370px;text-align:center;font-family:"Outfit",sans-serif;font-size:11.5px;color:var(--navy)}
  .authors{position:absolute;top:417px;font-family:"Outfit",sans-serif;font-size:11.5px;line-height:14.75px;color:var(--navy);list-style:none}
  .authors.col-a{left:171px}
  .authors.col-b{left:317px}

  .publisher-band{position:absolute;left:0;top:613px;width:646px;height:218px;background:var(--ink)}
  .about-heading{position:absolute;left:0;width:556px;top:634px;text-align:center;font-family:"Outfit",sans-serif;font-size:11.5px;color:var(--white)}
  .about-text{position:absolute;left:95px;width:363px;top:649px;font-family:"Outfit",sans-serif;font-size:11.4px;line-height:14.75px;color:var(--white);text-align:justify}

  /* spine */
  .spine-flourish{position:absolute;left:560px;top:0;width:70px;height:613px}
  .spine-title{position:absolute;left:572px;top:84px;height:504px;writing-mode:vertical-rl;white-space:nowrap;color:var(--white);display:flex;align-items:center;justify-content:space-between}
  .spine-title .script{font-family:"Great Vibes",cursive;font-size:60px;line-height:1}
  .spine-title .serif{font-family:"Playfair Display",serif;font-weight:700;font-size:30px;line-height:1;color:var(--ink);margin:0 4px}
  .spine-publisher{position:absolute;left:579px;top:650px;writing-mode:vertical-rl;font-family:"Outfit",sans-serif;font-size:10px;color:var(--white);letter-spacing:.2px;white-space:nowrap}
  .spine-dot{position:absolute;left:598px;top:710px;width:23px;height:23px;border-radius:50%;background:var(--white)}

  /* front cover */
  .front-title{position:absolute;left:646px;top:0;width:554px;height:300px}
  .front-title .script{position:absolute;font-family:"Great Vibes",cursive;font-weight:400;color:var(--white);line-height:1}
  .front-title .the{left:40px;top:10px;font-size:130px}
  .front-title .ascent{left:160px;top:120px;font-size:150px}
  .front-title .serif{position:absolute;left:0;width:554px;text-align:center;top:108px;font-family:"Playfair Display",serif;font-weight:700;font-size:52px;line-height:1;letter-spacing:3px;color:var(--ink)}

  .butterfly-art{position:absolute;left:738px;top:326px;width:372px;height:278px;
    background:radial-gradient(ellipse at 50% 70%,var(--wing-bright) 0%,#145a92 35%,var(--wing-deep) 75%,rgba(11,26,60,0) 100%);
    border-radius:45% 45% 40% 40%}

  .front-subtitle{position:absolute;left:700px;width:450px;top:673px;text-align:center;font-family:"Bodoni Moda",serif;font-size:17px;line-height:17px;letter-spacing:.5px;text-transform:uppercase;color:var(--white)}
  .imprint{position:absolute;left:646px;width:554px;top:754px;display:flex;flex-direction:column;align-items:center;gap:4px;font-family:"Outfit",sans-serif;font-size:16px;line-height:20px;color:var(--ink)}
  .imprint .mark{width:30px;height:30px;border-radius:50%;background:var(--ink)}
</style>
</head>
<body>
<main class="cover">

  <h2 class="back-title">THE QUIET ASCENT</h2>
  <p class="back-subtitle">Lessons of insight from a circle of mentors<br>to guide you toward a fuller journey</p>
  <div class="blurb">
    <p>A coach does not fix you. Or heal you. They coach you - by offering thoughts to ponder, guidance, techniques to try - All to help you play and succeed at the game of life.</p>
    <p>Each coach has their own personality, training, experience, method and philosophy they bring to the table. The underlying purpose is to guide you through the quiet ascent, to become the person you desire and aspire to be. Different coaches for different folks, yet they all have their own unique wisdom and special sauce to share.</p>
    <p>This book is a collection of just that. A tasting of the wisdom and philosophies of a variety of different coaches for you to experience.</p>
  </div>
  <p class="authors-heading">Authors names</p>
  <ul class="authors col-a">
    <li>Author name</li><li>Author name</li><li>Author name</li><li>Author name</li><li>Author name</li>
    <li>Author name</li><li>Author name</li><li>Author name</li><li>Author name</li><li>Author name</li>
  </ul>
  <ul class="authors col-b">
    <li>Author name</li><li>Author name</li><li>Author name</li><li>Author name</li><li>Author name</li>
    <li>Author name</li><li>Author name</li><li>Author name</li><li>Author name</li><li>Author name</li>
  </ul>

  <div class="publisher-band"></div>
  <p class="about-heading">About the Publisher</p>
  <p class="about-text">The Lark Publishing House is the publishing arm of The Lark Wellness Collective, a company founded and led by Dr. Marisol Aldane DPT in order to engage, educate, inspire, and empower healing and love within yourself and for others. The Lark Publishing House seeks to unlock the true potential of each individual to amplify their voice and message and to improve our human experience. Please visit https://thelarkwellness.net to learn about future publications.</p>

  <svg class="spine-flourish" viewBox="0 0 70 613" aria-hidden="true">
    <path d="M26 0 C 8 40, 30 70, 28 90" fill="none" stroke="#fff" stroke-width="1.2"/>
    <path d="M38 520 C 44 560, 30 590, 38 613" fill="none" stroke="#fff" stroke-width="1.2"/>
  </svg>
  <div class="spine-title">
    <span class="script">the</span>
    <span class="serif">QUIET</span>
    <span class="script">ascent</span>
  </div>
  <span class="spine-publisher">THE LARK PUBLISHING HOUSE</span>
  <span class="spine-dot"></span>

  <h1 class="front-title">
    <span class="script the">the</span>
    <span class="serif">QUIET</span>
    <span class="script ascent">ascent</span>
  </h1>

  <div class="butterfly-art" role="img" aria-label="Photograph of a deep blue butterfly with wings spread, bright turquoise bands on the lower wings"></div>

  <p class="front-subtitle">Lessons of insight from a circle<br>of mentors to guide you<br>toward a fuller journey</p>

  <div class="imprint"><span class="mark"></span><span>The Lark Publishing House</span></div>

</main>
</body>
</html>
```